Regionale Imkerei sucht Etiketten-Design
Sehr gutes Endergebnis. Hochprofessionelle Abwicklung. Hat jeden Änderungswunsch zügig umgesetzt. Sehr angenehme, zielorientierte Kommunikation. Wirklich zu empfehlen, gerne wieder!
Zielgruppe
Mein Vater und ich haben eine regionale Hobbyimkerei, die wir nach und nach ausbauen wollen. Seit 1949 imkert unsere Familie. Ich bin in dritter Generation eingestiegen und möchte neben meinem know-how den Verkauf und das Marketing voran treiben um mit der Imkerei einen Nebenerwerb zu schaffen. Unsere Zielgruppe sind bewusste Verbraucher/innen, die gerne regional, hochqualitativ und nachhaltig einkaufen. Die meisten Honiggläser verkaufen wir direkt an der Haustür. Bis jetzt sind nur zwei Läden beliefert. Das soll sich dank musterwerkstatt ändern.
Aufgabenstellung
Ich habe eine Ausschreibung im PDF Format verfasst und beigefügt.
Was dort fehlt sind die Lagerungshinweise: kühl, trocken und dunkel lagern.
Für weitere Rückfragen gerne melden.

```html
<!DOCTYPE html>
<html lang="de">
<head>
<meta charset="utf-8">
<title>Sonnenwabe – Etiketten</title>
<link rel="stylesheet" href="https://fonts.googleapis.com/css2?family=Fira+Sans:ital,wght@0,300;0,400;1,300&family=Mr+Dafoe&display=swap">
<style>
  :root{
    --backdrop:#f0ae48;
    --white:#ffffff;
    --ink:#5a5a5a;
    --ink-dark:#1f1f1f;
    --brand-yellow:#f5c400;
    --honey-panel:#fdf7de;
    --honey-accent:#f9e79c;
    --forest-panel:#e4f1d7;
    --forest-accent:#cce5b1;
    --berry-panel:#fae6e5;
    --berry-accent:#f6cccb;
  }
  *{box-sizing:border-box;margin:0;padding:0}
  html,body{width:872px;height:1200px;overflow:hidden}
  body{background:var(--backdrop);font-family:"Fira Sans",sans-serif;font-weight:300;color:var(--ink)}
  .label-sheet{display:flex;flex-direction:column;gap:80px;padding:212px 16px 0}
  .label{display:flex;width:840px;height:205px;background:var(--white)}
  .label--honey{--panel:var(--honey-panel);--accent:var(--honey-accent)}
  .label--forest{--panel:var(--forest-panel);--accent:var(--forest-accent)}
  .label--berry{--panel:var(--berry-panel);--accent:var(--berry-accent)}
  .label__facts{width:184px;background:var(--panel);display:flex;flex-direction:column;align-items:center;text-align:center;padding:16px 10px 14px;font-size:11.5px;line-height:13.8px}
  .facts__origin{height:58px}
  .facts__weight{font-size:19px;font-weight:400;color:#444;margin-top:2px}
  .facts__bestbefore{margin-top:auto;margin-bottom:30px}
  .label__front{position:relative;width:376px;overflow:hidden;display:flex;flex-direction:column;align-items:center}
  .front__backdrop{position:absolute;left:75px;top:0;width:215px;height:205px;border-radius:40px;background:linear-gradient(160deg,var(--accent),transparent 85%);opacity:.75}
  .front__brand{position:relative;margin-top:62px;display:flex;align-items:center;gap:10px;font-size:46px;font-weight:400;color:var(--brand-yellow);line-height:1}
  .brand__dot{width:14px;height:14px;border-radius:50%;background:var(--brand-yellow)}
  .front__tagline{position:relative;margin-top:14px;font-family:"Mr Dafoe",cursive;font-size:25px;color:var(--ink-dark);transform:rotate(-4deg)}
  .front__web{position:relative;margin-top:10px;font-size:12px;font-style:italic;font-weight:400;color:var(--ink-dark)}
  .label__story{flex:1;background:var(--panel);text-align:center;padding:12px 12px 0;font-size:11.5px;line-height:13.8px}
  .story__text{font-style:italic}
  .story__address{margin-top:14px}
</style>
</head>
<body>
<main class="label-sheet">

  <article class="label label--honey">
    <section class="label__facts">
      <p class="facts__origin">Honig aus deutscher Herstellung.<br>Blütenhonig aus Linden- und Rapsblüten.</p>
      <p class="facts__weight">250 g</p>
      <p class="facts__bestbefore">Mindestens haltbar bis:</p>
      <p class="facts__deposit">Mehrwegglas</p>
    </section>
    <section class="label__front">
      <div class="front__backdrop" role="img" aria-label="Gemalte Wabenform als Hintergrunddekor"></div>
      <h2 class="front__brand"><span class="brand__dot"></span>Sonnenwabe</h2>
      <p class="front__tagline">Blütenhonig aus der Region</p>
      <p class="front__web">www.tannenfrost.de</p>
    </section>
    <section class="label__story">
      <p class="story__text">Wir sind eine Familienimkerei. Wir erzeugen bereits seit 1949… Ihillest occab inctus et qui dolupta turehenis ma sum quis exeri con eatumqu ibernatia de is evelloris et et voluptas re, consequodi beatur alique ligeniatur? Dit re niminih icimus porrum Pidelenda aut aut alibus-antin porrovi dentiorior as naturero te lam nat que esequo moluptibus re nusdae pa nobissit aborita dolorero desedi</p>
      <p class="story__address">Imkerei Tannenfrost<br>Musterstraße 1, 12345 Musterstadt</p>
    </section>
  </article>

  <article class="label label--forest">
    <section class="label__facts">
      <p class="facts__origin">Honig aus deutscher Herstellung.<br>Blütenhonig aus Waldblüten.</p>
      <p class="facts__weight">250 g</p>
      <p class="facts__bestbefore">Mindestens haltbar bis:</p>
      <p class="facts__deposit">Mehrwegglas</p>
    </section>
    <section class="label__front">
      <div class="front__backdrop" role="img" aria-label="Gemalte Wabenform als Hintergrunddekor"></div>
      <h2 class="front__brand"><span class="brand__dot"></span>Sonnenwabe</h2>
      <p class="front__tagline">Waldblütenhonig aus der Region</p>
      <p class="front__web">www.tannenfrost.de</p>
    </section>
    <section class="label__story">
      <p class="story__text">Wir sind eine Familienimkerei. Wir erzeugen bereits seit 1949… Ihillest occab inctus et qui dolupta turehenis ma sum quis exeri con eatumqu ibernatia de is evelloris et et voluptas re, consequodi beatur alique ligeniatur? Dit re niminih icimus porrum Pidelenda aut aut alibus-antin porrovi dentiorior as naturero te lam nat que esequo moluptibus re nusdae pa nobissit aborita dolorero desedi</p>
      <p class="story__address">Imkerei Tannenfrost<br>Musterstraße 1, 12345 Musterstadt</p>
    </section>
  </article>

  <article class="label label--berry">
    <section class="label__facts">
      <p class="facts__origin">Honig aus deutscher Herstellung.<br>Blütenhonig Himbeer- und Johannisbeerblüten.</p>
      <p class="facts__weight">250 g</p>
      <p class="facts__bestbefore">Mindestens haltbar bis:</p>
      <p class="facts__deposit">Mehrwegglas</p>
    </section>
    <section class="label__front">
      <div class="front__backdrop" role="img" aria-label="Gemalte Wabenform als Hintergrunddekor"></div>
      <h2 class="front__brand"><span class="brand__dot"></span>Sonnenwabe</h2>
      <p class="front__tagline">Blütenhonig aus der Region</p>
      <p class="front__web">www.tannenfrost.de</p>
    </section>
    <section class="label__story">
      <p class="story__text">Wir sind eine Familienimkerei. Wir erzeugen bereits seit 1949… Ihillest occab inctus et qui dolupta turehenis ma sum quis exeri con eatumqu ibernatia de is evelloris et et voluptas re, consequodi beatur alique ligeniatur? Dit re niminih icimus porrum Pidelenda aut aut alibus-antin porrovi dentiorior as naturero te lam nat que esequo moluptibus re nusdae pa nobissit aborita dolorero desedi</p>
      <p class="story__address">Imkerei Tannenfrost<br>Musterstraße 1, 12345 Musterstadt</p>
    </section>
  </article>

</main>
</body>
</html>
```